Landscape Contractor in need of New Web Design

HELP.. Please Help!!!!. Our current website is old, outdated, ugly... and well nothing like us.... so we are looking for someone to help build a new website that fits our company direction. We are a landscape company with multiple locations in order to meet the needs of our clients and their projects throughout the midwest. When most people think of landscaping, they think of mowing grandmas yard, but that is NOT even remotely close to what we do. We are 100% a commercial landscape company meaning we complete landscape and irrigation services for large scale commercial projects. We are looking for a website to showcase our commercial talents and awesome team of people.
Updates

Address of current website is www.plovermeadowco.com

```html
<!DOCTYPE html>
<html lang="en">
<head>
<meta charset="utf-8">
<title>Plover Meadow Co. – Home Page Design</title>
<link rel="stylesheet" href="https://fonts.googleapis.com/css2?family=Lato:wght@400;700;900&display=swap">
<style>
:root{
  --lime:#8fe21a;
  --lime-dark:#5fae12;
  --green:#2f9e3c;
  --forest:#1f4a1a;
  --charcoal:#3d3d3d;
  --ink:#141414;
  --paper:#ffffff;
  --stage:#e4e4e4;
  --text:#222;
}
*{box-sizing:border-box;margin:0;padding:0}
html,body{width:1200px;height:708px;overflow:hidden;background:var(--stage);font-family:"Lato",Arial,sans-serif;color:var(--text)}
.page{position:absolute;left:495px;top:9px;width:600px;height:1968px;transform:scale(.35);transform-origin:0 0;background:var(--paper);overflow:hidden;box-shadow:0 20px 60px rgba(0,0,0,.25)}
.photo{display:block}

/* top bar */
.topbar{height:17px;background:var(--ink);color:#ddd;font-size:5px;display:flex;align-items:center;justify-content:center;gap:14px}
.topbar .quote-btn{background:var(--lime);color:var(--ink);padding:2px 5px;font-weight:700}
/* nav */
.nav{height:34px;display:flex;align-items:center;justify-content:space-between;padding:0 130px 0 125px}
.brand{display:flex;align-items:center;gap:4px;font-weight:700;font-size:8px;color:var(--forest)}
.brand .dot{width:9px;height:9px;border-radius:50%;background:var(--lime)}
.nav ul{list-style:none;display:flex;gap:12px;font-size:5px}

/* hero */
.hero{position:relative;height:185px;background:linear-gradient(90deg,#17300f,#2c5a1c 55%,#3d7a22);overflow:hidden}
.hero-copy{position:absolute;left:125px;top:34px;color:#fff}
.hero-copy .welcome{font-size:9px}
.hero-copy h1{font-weight:400;font-size:18px;line-height:1.1;margin-top:12px}
.hero-copy h1 .hl{color:var(--lime)}
.btns{display:flex;gap:6px;margin-top:12px}
.btn{font-size:4px;padding:3px 8px;background:var(--lime);color:var(--ink);font-weight:700}
.btn.alt{background:#777;color:#fff}
.hero-ring{position:absolute;right:-8px;top:-8px;width:300px;height:196px;border-radius:50%;border:5px solid var(--ink);background:var(--paper)}
.hero-photo{position:absolute;right:0;top:0;width:288px;height:184px;border-radius:50%;background:radial-gradient(circle at 45% 50%,#8c6a45,#5e7d2e 60%,#3a6a1f)}

/* about */
.about{position:relative;height:258px;background:var(--paper)}
.about-photo{position:absolute;left:125px;top:22px;width:170px;height:168px;border-radius:50% 50% 50% 12%;background:linear-gradient(160deg,#a9b98a,#4f8a2a 55%,#3b3b36)}
.about-card{position:absolute;left:294px;top:53px;width:182px;height:183px;background:var(--charcoal);border-radius:90px 90px 0 90px;color:#eee;padding:30px 22px 0 44px;font-size:4.5px;line-height:1.45}
.about-card h2{font-size:8px;font-weight:400;margin-bottom:7px}
.about-card .kicker{color:var(--lime);font-weight:700}
.about-card .btn{display:inline-block;margin-top:6px}

/* services */
.services{height:404px;background:var(--charcoal);padding:10px 20px 0}
.section-title{text-align:center;font-size:16px;font-weight:400;color:#fff}
.svc-grid{display:grid;grid-template-columns:repeat(3,172px);gap:22px 22px;justify-content:space-between;margin-top:10px}
.svc{position:relative;height:162px;display:flex;align-items:flex-end;justify-content:center;padding-bottom:12px;font-size:12px;color:var(--ink)}
.svc::after{content:"";position:absolute;inset:45% 0 0;background:linear-gradient(transparent,#fff 95%)}
.svc span{position:relative;z-index:1}
.svc.feature{background:linear-gradient(#7ec31a,var(--lime));align-items:center;text-align:center;padding:0}
.svc.feature::after{display:none}

/* why */
.why{position:relative;height:308px;background:var(--paper);padding-top:18px}
.why .section-title{color:var(--ink)}
.why-grid{display:grid;grid-template-columns:repeat(3,88px);justify-content:center;column-gap:44px;row-gap:10px;margin-top:14px}
.reason{text-align:center;font-size:6px}
.reason .tile{width:88px;height:88px;background:linear-gradient(145deg,var(--lime),#5fb71a);display:flex;align-items:center;justify-content:center;margin-bottom:8px;box-shadow:0 4px 6px rgba(0,0,0,.2)}
.reason .tile.dark{background:#3a3a3a;color:#ddd;font-size:4px;padding:14px;line-height:1.4}

/* we are */
.we-are{position:relative;height:189px;background:#1d1d1d;color:#fff;text-align:center;padding-top:16px}
.we-are p{font-size:5px;color:#ccc;margin-top:4px}
.gallery{display:flex;gap:10px;justify-content:center;margin-top:20px}
.gallery .photo{width:122px;height:88px}
.arrow{position:absolute;top:105px;font-size:14px;color:#ccc}
.grass-edge{position:absolute;left:0;right:0;bottom:0;height:28px;background:linear-gradient(#1d1d1d,#6fc21d)}

/* quote */
.quote{position:relative;height:231px;background:linear-gradient(90deg,#1f8a35,#2faa4a 60%,#25963e);color:#fff}
.quote-ring{position:absolute;left:-8px;top:8px;width:220px;height:190px;border-radius:50%;border:5px solid #fff;background:radial-gradient(circle,#8c6a45,#4f8a2a 65%)}
.quote-form{position:absolute;left:236px;top:16px;width:245px}
.quote-form h2{font-size:16px;font-weight:700}
.field{border-bottom:1px solid rgba(255,255,255,.6);font-size:4px;padding:12px 0 3px}
.field-row{display:flex;gap:20px}
.field-row .field{flex:1}
.quote-form .btn{display:block;width:40px;margin:18px auto 0;text-align:center}

/* testimonials */
.testimonials{height:182px;text-align:center;padding-top:18px}
.testimonials h2{font-size:15px;font-weight:400}
.testimonials .mark{font-size:22px;color:#ccc;line-height:.8}
.testimonials blockquote{width:330px;margin:4px auto 0;font-size:5px;line-height:1.5}
.stars{color:#f2b01e;font-size:7px;margin-top:6px}
.cite{font-size:5px;font-style:italic;color:#234;font-weight:700;margin-top:4px}
.dots{display:flex;gap:4px;justify-content:center;margin-top:12px}
.dots i{width:3px;height:3px;border-radius:50%;background:var(--green)}
.rule{width:440px;height:1px;background:#ddd;margin:14px auto 0}

/* footer */
.footer{position:relative;height:160px;background:linear-gradient(#183415,#0e1e0c);color:#ddd;font-size:4px}
.footer .brand{position:absolute;left:270px;top:12px;color:#fff}
.foot-cols{position:absolute;left:125px;top:56px;display:flex;gap:26px}
.foot-cols h3{font-size:5px;font-weight:700;margin-bottom:5px}
.foot-cols li{list-style:none;line-height:1.7}
.foot-cols li::before{content:"› ";color:var(--lime)}
.legal{position:absolute;left:125px;right:125px;bottom:8px;display:flex;justify-content:space-between}
.foot-photo{position:absolute;right:-14px;top:-4px;width:128px;height:148px;border-radius:50%;border:5px solid #fff;background:linear-gradient(#9aa59a,#4d8a2c)}
</style>
</head>
<body>
<main class="page">
  <div class="topbar">
    <span>Business Hours: 8am – 5pm / Mon – Fri</span>
    <span>(555) 764-0131</span><span>(555) 492-0126</span>
    <span>Contact Us ▾</span><span>Make A Payment ▾</span>
    <span class="quote-btn">GET A QUOTE</span>
  </div>
  <nav class="nav">
    <div class="brand"><span class="dot"></span>Plover Meadow Co.</div>
    <ul><li>Home</li><li>Divisions</li><li>Services</li><li>About Us</li><li>Gallery</li><li>Contact</li></ul>
  </nav>

  <section class="hero">
    <div class="hero-copy">
      <p class="welcome">Welcome To Plover Meadow Co.</p>
      <h1><span class="hl">15 Years</span><br>Of Professional<br>Landscaping!</h1>
      <div class="btns"><span class="btn">More About Us</span><span class="btn alt">Contact Us</span></div>
    </div>
    <div class="hero-ring"></div>
    <div class="photo hero-photo" role="img" aria-label="Gloved hands unrolling fresh sod"></div>
  </section>

  <section class="about">
    <div class="photo about-photo" role="img" aria-label="Winding garden path leading to a house"></div>
    <div class="about-card">
      <h2>About Us</h2>
      <p class="kicker">WE ARE PLOVER MEADOW CO.</p>
      <p>Founded by Evan Hart and Adam Brenner, Plover Meadow is the premier landscape maintenance and design company based in Cedar Falls, Kansas. Our company's dedication to innovative design projects created some of the most distinguished landscape projects throughout Kansas, Missouri, and Oklahoma.</p>
      <span class="btn">Read More</span>
    </div>
  </section>

  <section class="services">
    <h2 class="section-title">SERVICES</h2>
    <div class="svc-grid">
      <div class="svc photo" role="img" aria-label="Lawn mower on green grass" style="background:linear-gradient(#3f6e2a,#6aa43a)"><span>Maintenance</span></div>
      <div class="svc feature"><span>Chemical<br>Applications<br>&amp; Fertilization</span></div>
      <div class="svc photo" role="img" aria-label="Sprinkler watering turf" style="background:linear-gradient(#c8d8b4,#7fb24a)"><span>Turf Management</span></div>
      <div class="svc photo" role="img" aria-label="Worker laying sod rolls" style="background:linear-gradient(#4a6a8a,#7a9a4a)"><span>Hardscaping</span></div>
      <div class="svc photo" role="img" aria-label="Pink hibiscus flower bed" style="background:linear-gradient(#8aa86a,#c46a8a)"><span>Irrigation</span></div>
      <div class="svc photo" role="img" aria-label="Landscaped flower beds in front of a house" style="background:linear-gradient(#9a9a9a,#5a8a3a)"><span>Landscaping</span></div>
    </div>
  </section>

  <section class="why">
    <h2 class="section-title">WHY CHOOSE US?</h2>
    <div class="why-grid">
      <div class="reason"><div class="tile"><svg width="40" height="40" viewBox="0 0 40 40" fill="#fff"><path d="M20 34C20 22 8 20 6 8c10 0 14 8 14 18 0-10 4-18 14-18-2 12-14 14-14 26z"/></svg></div>Specialized Company</div>
      <div class="reason"><div class="tile dark">Rest assured knowing that our crew is fully licensed and insured and has a superior safety rating.</div>Licensed &amp; Insured</div>
      <div class="reason"><div class="tile"><svg width="44" height="40" viewBox="0 0 44 40" fill="#fff"><path d="M12 4l8 14h-4l6 10H2l6-10H4z M32 4l8 14h-4l6 10H22l6-10h-4z"/><rect x="10" y="28" width="4" height="8"/><rect x="30" y="28" width="4" height="8"/><rect x="2" y="36" width="40" height="2"/></svg></div>Dependable Services</div>
      <div class="reason"><div class="tile"><svg width="40" height="40" viewBox="0 0 40 40" fill="#fff"><rect x="6" y="4" width="5" height="22" transform="rotate(-40 8 15)"/><path d="M20 22l10-4 6 12-10 6-8-8z"/></svg></div>Day Scheduling</div>
      <div class="reason"><div class="tile"><svg width="30" height="40" viewBox="0 0 30 40" fill="#fff"><path d="M15 4C10 14 4 20 4 27a11 11 0 0 0 22 0C26 20 20 14 15 4z"/></svg></div>Free Consultations</div>
      <div class="reason"><div class="tile"><svg width="40" height="40" viewBox="0 0 40 40" fill="#fff"><rect x="6" y="18" width="7" height="16"/><path d="M15 18l6-12c3 0 4 2 3 6l-1 4h9c2 0 3 2 2 4l-3 12c-1 2-2 2-4 2H15z"/></svg></div>Dependable Services</div>
    </div>
  </section>

  <section class="we-are">
    <h2 class="section-title">WE ARE</h2>
    <p>Plover Meadow Co. is a full service lawn and landscape contractor providing design, installation, and maintenance services.</p>
    <span class="arrow" style="left:14px">‹</span><span class="arrow" style="right:14px">›</span>
    <div class="gallery">
      <div class="photo" role="img" aria-label="Garden bench among plants" style="background:linear-gradient(#6a8a4a,#8ab85a)"></div>
      <div class="photo" role="img" aria-label="Green lawn gallery tile" style="background:linear-gradient(#3ea83e,#62c04a)"></div>
      <div class="photo" role="img" aria-label="White park bench on a lawn" style="background:linear-gradient(#8aa86a,#5a9a3a)"></div>
      <div class="photo" role="img" aria-label="Pergola over a patio garden" style="background:linear-gradient(#7a7a6a,#5a9a3a)"></div>
    </div>
    <div class="grass-edge" role="img" aria-label="Grass edge"></div>
  </section>

  <section class="quote">
    <div class="quote-ring photo" role="img" aria-label="Worker unrolling sod"></div>
    <form class="quote-form">
      <h2>REQUEST A QUICK QUOTE</h2>
      <div class="field">Your Name</div>
      <div class="field-row"><div class="field">Your Email</div><div class="field">Snow Removal</div></div>
      <div class="field" style="height:46px">Your Message</div>
      <span class="btn">Submit</span>
    </form>
  </section>

  <section class="testimonials">
    <h2>TESTIMONIALS</h2>
    <div class="mark">“</div>
    <blockquote>I went by Linden Grove again this morning and checked the work performed recently. All areas look very nice and it looks like we received more sod north of the playground than I expected, which made the principal happy. I am very pleased with the work performed by Plover Meadow and the cooperation from you on the out of your control delays in schedule and revisions to the scope of work. It has been a pleasant experience. Thanks.</blockquote>
    <div class="stars">★★★★★</div>
    <div class="cite">Rick Farrow – Prairie Valley School District</div>
    <div class="dots"><i></i><i></i><i></i><i></i><i></i></div>
    <div class="rule"></div>
  </section>

  <footer class="footer">
    <div class="brand"><span class="dot"></span>Plover Meadow Co.</div>
    <div class="foot-cols">
      <div style="width:90px"><h3>ABOUT</h3><p style="line-height:1.6">Plover Meadow strives to set the standard for the highest quality lawn and landscape products and services and to exceed our customer's expectations every time.</p></div>
      <div><h3>OUR SERVICES</h3><ul><li>Turf Management</li><li>Hardscaping</li><li>Irrigation</li><li>Landscaping</li></ul></div>
      <div><h3>QUICK LINKS</h3><ul><li>About Us</li><li>Divisions</li><li>Certifications</li><li>Gallery</li></ul></div>
      <div><h3>CONTACT</h3><ul><li>Plover Meadow Co., 120 Elm Street</li><li>Main Office: (555) 764-0131</li><li>North Office: (555) 492-0126</li></ul></div>
    </div>
    <div class="photo foot-photo" role="img" aria-label="Pergola in a landscaped garden"></div>
    <div class="legal"><span>Copyright © Plover Meadow Co.</span><span>Terms &amp; Conditions | Privacy Policy</span><span></span></div>
  </footer>
</main>
</body>
</html>
```